Toravex Systems Brochure

I am looking for a brochure layout, either a tri fold or double fold which ever fits the design better. I have listed a little info below concerning the services Toravex Tech provides.

The name of my company is Toravex Systems, that offers a wide range of services. Services that we offer are (Fiber optic solutions, Audio visual services, voice and date infrastructure, wireless capabilities, and sound system design). We have done work for a wide range of clients ranges from small offices to major retail stores. I would like to create a brochure that helps market my company. Something to hand to my customers on the job therefore they will have a great idea of all the services that we offer. I really like the idea of a roadmap, for example if there was a picture of an office area we could have an arrow pointing to the conference room and say audio visual solutions and give a little blurb about what that exactly means. (short and concise). To help describe some of our services you can look at our website to get a better idea of what exactly it is that we offer. http://www.toravexsys-example.com/ Look forward to hearing back from you and seeing what you can come up with for us!
Updates

Target Market(s)

current and future clients, interested in upgrading their current technology infrastructure.

Colors

Designer to choose colors to be used in the design.

Requirements
Must have
• Services offered
• Brief explanation of services offered
• Contact information
Nice to have
• Why choose Toravex section.

```html
<!DOCTYPE html>
<html lang="en">
<head>
<meta charset="utf-8">
<title>Toravex Systems Brochure</title>
<link rel="stylesheet" href="https://fonts.googleapis.com/css2?family=Lato:wght@400;700&family=Tinos:wght@400;700&family=Roboto+Condensed:wght@700&display=swap">
<style>
  :root {
    --brand-blue: #2270b4;
    --brand-green: #6ab345;
    --ink: #1d1d1d;
    --soft-ink: #333;
    --paper: #ffffff;
  }
  * { margin: 0; padding: 0; box-sizing: border-box; }
  html, body { width: 1200px; height: 1029px; overflow: hidden; background: var(--paper); }
  .spread { position: relative; width: 1200px; height: 1029px; font-family: "Lato", sans-serif; color: var(--soft-ink); }
  .page { position: absolute; top: 0; width: 600px; height: 1029px; overflow: hidden; }
  .page--back { left: 0; background: #f7f7f7; }
  .page--cover { left: 600px; background: var(--paper); }
  .shapes { position: absolute; inset: 0; }

  .cable-photo { position: absolute; left: 170px; top: 150px; width: 430px; height: 470px;
    background: radial-gradient(ellipse at 65% 45%, #dcdcdc 0%, #e9e9e9 45%, rgba(247,247,247,0) 75%); }

  .services-title { position: absolute; left: 58px; top: 56px; font-family: "Tinos", serif; font-weight: 700;
    font-size: 32px; color: var(--brand-green); }
  .service { position: absolute; font-size: 20px; line-height: 26px; color: var(--soft-ink); padding-left: 22px; }
  .service::before { content: ""; position: absolute; left: 0; top: 9px; width: 10px; height: 10px; border-radius: 50%; background: var(--brand-green); }
  .service--mid::before { top: 22px; }

  .back-name { position: absolute; left: 62px; top: 650px; font-family: "Tinos", serif; font-size: 24px;
    color: var(--paper); letter-spacing: 0.5px; }
  .contact { position: absolute; left: 55px; font-size: 20px; line-height: 27px; color: var(--paper); display: flex; gap: 14px; align-items: flex-start; white-space: nowrap; }
  .contact svg { flex: none; margin-top: 3px; }
  .network-map { position: absolute; left: 294px; top: 729px; width: 282px; height: 128px; border: 3px solid var(--paper);
    background: linear-gradient(135deg, #d7d4cc, #b7b2a6 55%, #8f8a80); box-shadow: 0 8px 14px rgba(0,0,0,0.25); }

  .cover-name { position: absolute; left: 0; width: 600px; top: 160px; text-align: center; font-family: "Tinos", serif;
    font-size: 34px; color: #2a2a2a; letter-spacing: 1px; }
  .city-photo { position: absolute; left: 0; top: 110px; width: 600px; height: 600px;
    background: linear-gradient(180deg, rgba(255,255,255,1) 0%, rgba(255,255,255,0) 30%),
                radial-gradient(circle at 62% 42%, #f4f8ff 0%, #9fb9e6 14%, #4a73bf 40%, #2c4f93 70%, #1d3c78 100%); }

  .headline { font-weight: 400; }
  .headline span { position: absolute; right: 58px; line-height: 1; white-space: nowrap; }
  .headline__top { top: 760px; font-family: "Roboto Condensed", sans-serif; font-weight: 700; font-size: 64px; color: var(--brand-blue); }
  .headline__mid { top: 826px; font-family: "Tinos", serif; font-weight: 700; font-size: 54px; color: var(--brand-green); }
  .headline__end { top: 884px; font-family: "Tinos", serif; font-weight: 400; font-size: 56px; color: var(--ink); }
  .cover-url { position: absolute; right: 58px; top: 952px; font-size: 26px; letter-spacing: 6px; color: var(--ink); white-space: nowrap; }
</style>
</head>
<body>
<main class="spread">

  <section class="page page--back">
    <div class="cable-photo" role="img" aria-label="Faded photo of network patch cables plugged into a switch"></div>
    <svg class="shapes" width="600" height="1029" viewBox="0 0 600 1029">
      <polygon points="0,395 600,610 600,889 459,1029 0,1029" fill="var(--brand-blue)"/>
      <polygon points="459,1029 600,889 600,1029" fill="var(--paper)"/>
    </svg>

    <h2 class="services-title">We offer are</h2>
    <p class="service" style="left:55px; top:128px;">Fiber optic<br>solutions</p>
    <p class="service" style="left:55px; top:203px;">Audio visual<br>services</p>
    <p class="service service--mid" style="left:55px; top:276px;">Voice and date<br>infrastructure</p>
    <p class="service" style="left:313px; top:130px;">Wireless<br>capabilities</p>
    <p class="service" style="left:313px; top:204px;">Sound system design</p>

    <p class="back-name">Toravex Systems</p>

    <div class="contact" style="top:717px;">
      <svg width="20" height="24" viewBox="0 0 20 24"><path d="M10 0a8 8 0 0 0-8 8c0 6 8 15 8 15s8-9 8-15a8 8 0 0 0-8-8zm0 11a3 3 0 1 1 0-6 3 3 0 0 1 0 6z" fill="var(--brand-green)"/></svg>
      <span>14-C Calder Road<br>Easton, MA 02390</span>
    </div>
    <div class="contact" style="top:792px;">
      <svg width="22" height="22" viewBox="0 0 24 24"><path d="M6.6 10.8a15 15 0 0 0 6.6 6.6l2.2-2.2a1 1 0 0 1 1-.25 11 11 0 0 0 3.6.6 1 1 0 0 1 1 1V20a1 1 0 0 1-1 1A17 17 0 0 1 3 4a1 1 0 0 1 1-1h3.5a1 1 0 0 1 1 1 11 11 0 0 0 .6 3.6 1 1 0 0 1-.25 1z" fill="var(--brand-green)"/></svg>
      <span>555-014-2270</span>
    </div>
    <div class="contact" style="top:840px;">
      <svg width="24" height="22" viewBox="0 0 24 22"><rect x="6" y="0" width="12" height="6" fill="var(--brand-green)"/><rect x="0" y="7" width="24" height="9" rx="2" fill="var(--brand-green)"/><rect x="6" y="14" width="12" height="8" fill="var(--brand-green)" stroke="var(--brand-blue)" stroke-width="1.5"/></svg>
      <span>555-014-2271</span>
    </div>
    <div class="contact" style="top:887px;">
      <svg width="22" height="18" viewBox="0 0 22 18"><rect x="1" y="2" width="20" height="14" fill="none" stroke="var(--brand-green)" stroke-width="2"/><path d="M1 2l10 8 10-8" fill="none" stroke="var(--brand-green)" stroke-width="2"/></svg>
      <span>info@toravexsys-example.com</span>
    </div>
    <div class="contact" style="top:928px;">
      <svg width="22" height="22" viewBox="0 0 22 22"><circle cx="11" cy="11" r="9" fill="none" stroke="var(--brand-green)" stroke-width="2"/><ellipse cx="11" cy="11" rx="4" ry="9" fill="none" stroke="var(--brand-green)" stroke-width="1.5"/><path d="M2 11h18" stroke="var(--brand-green)" stroke-width="1.5"/></svg>
      <span>www.toravexsys-example.com</span>
    </div>

    <div class="network-map" role="img" aria-label="Cabling diagram of an enterprise office and factory floor"></div>
  </section>

  <section class="page page--cover">
    <div class="city-photo" role="img" aria-label="City skyline at night with a world network map and a hand using a smartphone"></div>
    <p class="cover-name">Toravex Systems</p>
    <svg class="shapes" width="600" height="1029" viewBox="0 0 600 1029">
      <polygon points="0,610 0,1029 600,1029 600,701 413,604 255,711" fill="var(--paper)"/>
      <polygon points="0,610 255,711 0,902" fill="var(--brand-green)"/>
      <polyline points="0,902 413,604 600,701" fill="none" stroke="var(--brand-blue)" stroke-width="9" stroke-linejoin="miter"/>
      <polygon points="0,902 413,604 600,701 600,1029 0,1029" fill="var(--paper)"/>
    </svg>
    <h1 class="headline">
      <span class="headline__top">YOUR IT</span>
      <span class="headline__mid">CONNECTION</span>
      <span class="headline__end">TO THE FUTURE</span>
    </h1>
    <p class="cover-url">www.toravexsys-example.com</p>
  </section>

</main>
</body>
</html>
```